BUSINESS book cover

Publishing a book for a specific industry and hope to customize it for different industries in the future. So, design needs to be flexible. I want BRIGHT (possibly orange) cover with large words for title...really do not need illustration. Just the subtitle will change for future editions. Book is going to be 5.25" x 8"

Sorry for any confusion. The title of the book is: "Where Stories Bend Sideways..." The subtitle is: A Comprehensive Member Expderience Guide for Today's Club Management Professional

```html
<!DOCTYPE html>
<html lang="en">
<head>
<meta charset="utf-8">
<title>Where Stories Bend Sideways... — Book Cover</title>
<link rel="stylesheet" href="https://fonts.googleapis.com/css2?family=Cinzel:wght@400;500;600;700&display=swap">
<style>
  :root {
    --orange-deep: #f39a1e;
    --orange-mid: #f9b43a;
    --glow: #fff1a8;
    --cream: #fff6c8;
    --gold-light: #fff4b0;
    --gold-mid: #e0b43a;
    --gold-dark: #8a5a08;
    --rule: #ffd24a;
  }
  html, body {
    margin: 0;
    padding: 0;
    width: 827px;
    height: 1200px;
    overflow: hidden;
  }
  .cover {
    position: relative;
    width: 827px;
    height: 1200px;
    overflow: hidden;
    background: radial-gradient(ellipse 520px 620px at 50% 42%, var(--glow) 0%, var(--orange-mid) 55%, var(--orange-deep) 100%);
    font-family: "Cinzel", "Trajan Pro", serif;
  }
  .author {
    position: absolute;
    top: 40px;
    left: 0;
    width: 100%;
    margin: 0;
    text-align: center;
    font-size: 60px;
    font-weight: 500;
    letter-spacing: 3px;
    color: var(--cream);
    text-shadow: 0 1px 2px rgba(150, 80, 0, 0.35);
  }
  .rule {
    position: absolute;
    left: 135px;
    width: 557px;
    height: 3px;
    background: linear-gradient(90deg, rgba(255, 210, 74, 0) 0%, var(--rule) 20%, var(--rule) 80%, rgba(255, 210, 74, 0) 100%);
  }
  .rule--top { top: 150px; }
  .rule--bottom { top: 1002px; }
  .title {
    position: absolute;
    top: 170px;
    left: 0;
    width: 827px;
    height: 820px;
  }
  .title text {
    font-family: "Cinzel", "Trajan Pro", serif;
    font-weight: 600;
    fill: url(#goldFill);
    stroke: var(--gold-dark);
    stroke-width: 1.2;
    filter: url(#bevelShadow);
  }
  .subtitle {
    position: absolute;
    top: 1038px;
    left: 40px;
    width: 747px;
    margin: 0;
    text-align: center;
    font-size: 31px;
    line-height: 38px;
    font-weight: 500;
    letter-spacing: 1px;
    color: var(--cream);
    text-shadow: 0 1px 2px rgba(150, 80, 0, 0.35);
  }
</style>
</head>
<body>
  <main class="cover">
    <p class="author">Dale Marrow</p>
    <div class="rule rule--top"></div>

    <svg class="title" viewBox="0 0 827 820" role="heading" aria-level="1" aria-label="Where Stories Bend Sideways...">
      <defs>
        <linearGradient id="goldFill" x1="0" y1="0" x2="0" y2="1">
          <stop offset="0" stop-color="var(--gold-light)" style="stop-color:#fff4b0"/>
          <stop offset="0.45" stop-color="#f0cc55"/>
          <stop offset="0.7" stop-color="#c99224"/>
          <stop offset="1" stop-color="#fbe08a"/>
        </linearGradient>
        <filter id="bevelShadow" x="-5%" y="-5%" width="110%" height="115%">
          <feDropShadow dx="2" dy="3" stdDeviation="2" flood-color="#9a5a00" flood-opacity="0.45"/>
        </filter>
      </defs>
      <text x="413.5" y="196" text-anchor="middle" font-size="190" textLength="620" lengthAdjust="spacingAndGlyphs">Where</text>
      <text x="413.5" y="384" text-anchor="middle" font-size="190" textLength="747" lengthAdjust="spacingAndGlyphs">Stories</text>
      <text x="413.5" y="557" text-anchor="middle" font-size="190" textLength="560" lengthAdjust="spacingAndGlyphs">Bend</text>
      <text x="413.5" y="721" text-anchor="middle" font-size="170" textLength="760" lengthAdjust="spacingAndGlyphs">Sideways...</text>
    </svg>

    <div class="rule rule--bottom"></div>
    <p class="subtitle">A Comprehensive Member Experience<br>Guide for Today's Club Management<br>Professional</p>
  </main>
</body>
</html>
```